Centro Renal Tova Quirandel

Redo a rough draft of the presentation. Some slides are just hand sketches. 15 slides total

Font styles to use
Sans Serif

Colors

Designer to choose colors to be used in the design.

Requirements
Must have
• Use the 'machine' on the dialysis slide. The kidney wherever you feel works to accentuate.
• The slide following the 'supporting cast' should be the same but 'centro vitrales norteños' in bold and maybe the picture vascular acces if works.
• Use the 4 puerto Halcón pictures for 'centro de dialisis puerto halcón' create 4 slides using one picture per slide; go big.
• Create a location slide before the last q&a slide using the location picture
Nice to have
• Please use elegant font for title
• Create something for the estadisticas 2016 slides; not a list like it is now

```html
<!DOCTYPE html>
<html lang="es">
<head>
<meta charset="utf-8">
<title>Centro Renal Tova Quirandel</title>
<link href="https://fonts.googleapis.com/css2?family=Tinos:wght@400;700&family=Roboto:wght@300;400;500&family=Dosis:wght@300;400;500&display=swap" rel="stylesheet">
<style>
:root{
  --maroon:#7e3a4c;
  --maroon-deep:#6a2f3f;
  --taupe:#b5aaa6;
  --taupe-light:#d8d1ce;
  --ink:#4a4044;
  --muted:#7a7275;
  --paper:#ffffff;
  --canvas:#ffffff;
  --line:#c9c1be;
}
*{margin:0;padding:0;box-sizing:border-box}
html,body{width:1200px;height:2769px;overflow:hidden;background:var(--canvas)}
body{position:relative;font-family:"Roboto",Arial,sans-serif;color:var(--ink)}
.slide{position:absolute;left:270px;width:661px;height:373px;background:var(--paper);overflow:hidden;box-shadow:0 2px 6px rgba(0,0,0,.18)}
.brand{position:absolute;display:flex;align-items:center;gap:6px;font-family:"Roboto",Arial,sans-serif;font-weight:400;color:var(--maroon);letter-spacing:.2px}
.brand-dot{border-radius:50%;background:var(--maroon)}
.brand-lg{font-size:30px}.brand-lg .brand-dot{width:26px;height:26px}
.brand-sm{font-size:12px}.brand-sm .brand-dot{width:10px;height:10px}
.footnote{position:absolute;right:24px;bottom:8px;font-size:6.5px;color:var(--muted);letter-spacing:.3px}
.base-band{position:absolute;left:0;right:0;bottom:0;height:20px;background:var(--taupe)}
.slide-title{position:absolute;left:20px;top:28px;font-family:"Tinos","Times New Roman",serif;font-weight:700;font-size:25px;color:var(--maroon);letter-spacing:.5px}
.slide-title::after{content:"";position:absolute;left:0;top:36px;width:36px;height:2px;background:var(--taupe)}
.foot-logo{position:absolute;left:0;bottom:20px;background:#fff;padding:4px 14px 4px 22px;border-radius:0 12px 0 0}

/* cover */
.cover-art{position:absolute;left:0;top:70px;width:661px;height:286px;background:linear-gradient(90deg,#dfe6ec 0%,#c7d3dd 35%,#e9e3e6 55%,#d9c8cf 75%,#cbd7e0 100%)}
.cover-plate{position:absolute;left:85px;top:123px;width:282px;height:250px;background:rgba(126,58,76,.9);display:flex;flex-direction:column;align-items:center;justify-content:center;padding-bottom:20px}
.cover-plate h1{font-family:"Tinos","Times New Roman",serif;font-weight:400;font-size:36px;line-height:1.18;color:#fff;text-align:center}
.cover-plate .rule{width:42px;height:2px;background:#fff;margin-top:14px}
.agency{position:absolute;right:14px;top:14px;display:flex;align-items:center;gap:6px;font-size:10px;font-weight:500;color:var(--maroon)}
.agency span{width:22px;height:22px;border-radius:50%;background:var(--taupe)}

/* profile */
.profile-panel{position:absolute;left:0;top:0;width:207px;height:373px;background:var(--maroon)}
.avatar{position:absolute;left:46px;top:129px;width:114px;height:114px;border-radius:50%;background:#e9e4e3}
.profile-name{position:absolute;left:225px;top:102px;font-family:"Dosis",Arial,sans-serif;font-weight:500;font-size:22px;color:var(--maroon-deep)}
.profile-rule{position:absolute;left:225px;top:134px;width:416px;height:1px;background:var(--line)}
.profile-list{position:absolute;left:225px;top:162px;list-style:none;font-family:"Dosis",Arial,sans-serif;font-weight:400;font-size:16.5px;line-height:27.5px;color:var(--muted)}
.profile-list li.wrap{line-height:20px;padding:4px 0}

/* section */
.section-photo{position:absolute;inset:0;background:linear-gradient(135deg,#9c5d6c 0%,#8c4a5c 45%,#a56a77 75%,#b8858f 100%)}
.section-icon{position:absolute;left:80px;top:165px}
.section-rule{position:absolute;left:40px;top:220px;width:621px;height:1px;background:rgba(255,255,255,.45)}
.section-title{position:absolute;left:65px;top:236px;font-family:"Tinos","Times New Roman",serif;font-weight:400;font-size:30px;line-height:1.25;color:#fff}

/* dialysis */
.modes{position:absolute;left:0;top:100px;width:661px;height:205px}
.mode{position:absolute;top:0;height:205px;color:#fff;text-align:center;padding:65px 22px 0}
.mode-acute{left:0;width:330px;background:linear-gradient(90deg,#7e3a4c,#8d4b5c)}
.mode-chronic{left:330px;width:331px;background:linear-gradient(90deg,#b3a5a5,#c7bcbb)}
.mode-badge{position:absolute;top:-30px;left:50%;margin-left:-30px;width:60px;height:60px;border-radius:50%;background:#fff;border:2px solid var(--maroon);display:flex;align-items:center;justify-content:center}
.mode-chronic .mode-badge{border-color:#c8bdbc;background:rgba(255,255,255,.35)}
.mode h3{font-weight:400;font-size:17px;margin-bottom:6px}
.mode p{font-weight:300;font-size:16px;line-height:20px}

/* stats */
.stats{position:absolute;left:20px;top:90px;width:621px}
.stat-row{display:flex;height:117px;background:var(--maroon);margin-bottom:3px}
.stat-row.alt{background:var(--taupe)}
.stat{flex:1;display:flex;flex-direction:column;align-items:center;justify-content:center;color:#fff;position:relative}
.stat+.stat::before{content:"";position:absolute;left:0;top:22px;bottom:22px;width:1px;background:rgba(255,255,255,.45)}
.stat-value{font-family:"Dosis",Arial,sans-serif;font-weight:400;font-size:36px;line-height:1}
.stat-value::after{content:"";display:block;width:58px;height:1px;background:rgba(255,255,255,.6);margin:8px auto 10px}
.stat-label{font-family:"Dosis",Arial,sans-serif;font-size:18px}

/* providers */
.provider{position:absolute;display:flex;align-items:center;justify-content:center;text-align:center;background:#fff;border:1px solid #e2dcdb;box-shadow:0 1px 4px rgba(0,0,0,.12);font-size:11px;font-weight:500;color:var(--maroon);line-height:1.2;padding:0 6px}
.agency-mark{position:absolute;font-size:13px;font-weight:500;color:var(--maroon);text-align:center}
.links{position:absolute;left:0;top:0}
</style>
</head>
<body>

<!-- 1 Cover -->
<section class="slide" style="top:9px">
  <div class="brand brand-lg" style="left:22px;top:18px"><span class="brand-dot"></span>nefralia</div>
  <div class="agency"><span></span>Salud Isleña</div>
  <div class="cover-art" role="img" aria-label="Ilustración de riñones humanos en tonos azul y rosa"></div>
  <div class="cover-plate">
    <h1>Centro Renal<br>Tova Quirandel</h1>
    <div class="rule"></div>
  </div>
  <div class="base-band"></div>
</section>

<!-- 2 Profile -->
<section class="slide" style="top:406px">
  <div class="profile-panel"></div>
  <div class="avatar" role="img" aria-label="Retrato de la directora médica"></div>
  <div class="brand brand-lg" style="right:20px;top:22px"><span class="brand-dot"></span>nefralia</div>
  <div class="profile-name">Marisol Etxeberri, MD</div>
  <div class="profile-rule"></div>
  <ul class="profile-list">
    <li>Board Certified in Nephrology</li>
    <li>Medical Director Vitalis Brisamar</li>
    <li>former:</li>
    <li>Nephrology Department Director Hospital Amparo Común</li>
    <li>Faculty Member, Isla Norte School of Medicine</li>
  </ul>
  <div class="footnote">© 2017 NEFRALIA · all rights reserved &nbsp;|&nbsp; 2</div>
</section>

<!-- 3 Profile -->
<section class="slide" style="top:801px">
  <div class="profile-panel"></div>
  <div class="avatar" role="img" aria-label="Retrato del ingeniero desarrollador"></div>
  <div class="brand brand-lg" style="right:20px;top:22px"><span class="brand-dot"></span>nefralia</div>
  <div class="profile-name">Ing. Tomás R. Quevedo</div>
  <div class="profile-rule"></div>
  <ul class="profile-list" style="left:228px">
    <li>B.A. Civil Engineering</li>
    <li class="wrap">Miembro Junta Directores Fundación<br>Insular del Riñón</li>
    <li>Desarrollador:</li>
    <li>Centro de Diálisis Puerto Halcón</li>
    <li>Arcángel Veluma Dialysis Centre</li>
  </ul>
  <div class="footnote">© 2017 NEFRALIA · all rights reserved &nbsp;|&nbsp; 3</div>
</section>

<!-- 4 Section -->
<section class="slide" style="top:1196px">
  <div class="section-photo" role="img" aria-label="Fotografía de una máquina de diálisis con filtro maroon"></div>
  <svg class="section-icon" width="26" height="36" viewBox="0 0 26 36" aria-hidden="true">
    <ellipse cx="7" cy="20" rx="6" ry="9" fill="none" stroke="#fff" stroke-width="1.6"/>
    <ellipse cx="19" cy="20" rx="6" ry="9" fill="none" stroke="#fff" stroke-width="1.6"/>
    <path d="M13 2 V12 M13 12 L9 18 M13 12 L17 18" stroke="#fff" stroke-width="1.6" fill="none"/>
  </svg>
  <div class="section-rule"></div>
  <h2 class="section-title">Centro de Diálisis Puerto<br>Halcón Arcángel</h2>
</section>

<!-- 5 Dialysis -->
<section class="slide" style="top:1591px">
  <h2 class="slide-title">DIALISIS</h2>
  <div class="modes" role="img" aria-label="Fondo fotográfico de equipo de diálisis bajo las dos columnas">
    <div class="mode mode-acute">
      <div class="mode-badge"><svg width="28" height="28" viewBox="0 0 28 28"><circle cx="14" cy="14" r="10" fill="none" stroke="#7e3a4c" stroke-width="2"/><circle cx="14" cy="14" r="4" fill="#7e3a4c"/></svg></div>
      <h3>Agudo</h3>
      <p>Tratamiento a pacientes con perdida repentina de función renal y usualmente temporera. Administrada en hospitales.</p>
    </div>
    <div class="mode mode-chronic">
      <div class="mode-badge"><svg width="28" height="28" viewBox="0 0 28 28"><circle cx="14" cy="14" r="10" fill="none" stroke="#fff" stroke-width="2"/><circle cx="14" cy="14" r="4" fill="#fff"/></svg></div>
      <h3>Crónico</h3>
      <p>Tratamiento a pacientes con perdida permanente de función renal.</p>
    </div>
  </div>
  <div class="base-band"></div>
  <div class="foot-logo"><div class="brand brand-sm" style="position:static"><span class="brand-dot"></span>nefralia</div></div>
  <div class="footnote" style="bottom:6px;color:#fff">© 2017 NEFRALIA · all rights reserved &nbsp;|&nbsp; 5</div>
</section>

<!-- 6 Stats -->
<section class="slide" style="top:1986px">
  <h2 class="slide-title">ESTADISTICAS 2016</h2>
  <div class="stats">
    <div class="stat-row">
      <div class="stat"><span class="stat-value">5841</span><span class="stat-label">PREVALENCIA</span></div>
      <div class="stat"><span class="stat-value">1140</span><span class="stat-label">Mortalidad</span></div>
      <div class="stat"><span class="stat-value">95</span><span class="stat-label">Transplantes</span></div>
    </div>
    <div class="stat-row alt">
      <div class="stat"><span class="stat-value">1428</span><span class="stat-label">INCIDENCIA</span></div>
      <div class="stat"><span class="stat-value">66%</span><span class="stat-label">Diabetes</span></div>
      <div class="stat"><span class="stat-value">20%</span><span class="stat-label">Hipertensión</span></div>
    </div>
  </div>
  <div class="base-band"></div>
  <div class="foot-logo"><div class="brand brand-sm" style="position:static"><span class="brand-dot"></span>nefralia</div></div>
  <div class="footnote" style="bottom:6px;color:#fff">© 2017 NEFRALIA · all rights reserved &nbsp;|&nbsp; 6</div>
</section>

<!-- 7 Providers -->
<section class="slide" style="top:2381px">
  <h2 class="slide-title">PROVEEDORES</h2>
  <svg class="links" width="661" height="373" aria-hidden="true">
    <path d="M183 144 L99 203 M183 144 L253 203" stroke="#b5aaa6" stroke-width="1.2" fill="none"/>
    <path d="M490 144 L490 198" stroke="#b5aaa6" stroke-width="1.2"/>
    <path d="M485 194 L490 202 L495 194 Z" fill="#b5aaa6"/>
  </svg>
  <div class="provider" style="left:114px;top:79px;width:139px;height:65px">Vitalis Medical Care</div>
  <div class="provider" style="left:420px;top:79px;width:141px;height:65px;font-weight:400">Costamar Healthcare Group</div>
  <div class="provider" style="left:30px;top:203px;width:138px;height:65px">Tríade Salud</div>
  <div class="provider" style="left:181px;top:203px;width:144px;height:65px">Pulso Salud Mayor</div>
  <div class="provider" style="left:420px;top:203px;width:140px;height:65px">Corvia Salud</div>
  <div class="agency-mark" style="left:96px;top:292px;width:160px">Federal Care Services</div>
  <div class="agency-mark" style="left:402px;top:292px;width:160px">Agencia Salud Isleña</div>
  <div class="base-band"></div>
  <div class="foot-logo"><div class="brand brand-sm" style="position:static"><span class="brand-dot"></span>nefralia</div></div>
  <div class="footnote" style="bottom:6px;color:#fff">© 2017 NEFRALIA · all rights reserved &nbsp;|&nbsp; 7</div>
</section>

</body>
</html>
```